Cedar Hall businesscard

We changed our name and logo, now we need new business cards.
3-4/71 Marlow Street Ridgeford 2163
www.cedarhallfellowship.example
info@cedarhallfellowship.example
Louise-Jane Tredwick
Senior Pastor
ph: 02 95558172

Industry/Entity Type

Business

```html
<!DOCTYPE html>
<html lang="en">
<head>
<meta charset="utf-8">
<title>Cedar Hall business card</title>
<link rel="stylesheet" href="https://fonts.googleapis.com/css2?family=Jost:wght@300;400&display=swap">
<style>
  :root {
    --backdrop: #4a4a4a;
    --card-white: #f5f5f5;
    --slate: #6d7f90;
    --slate-dark: #5e7387;
    --slate-light: #9fb0c0;
    --ink: #3a3a3a;
    --divider: #c9cfd5;
    --back-text: #f2f4f6;
  }
  * { margin: 0; padding: 0; box-sizing: border-box; }
  html, body {
    width: 1200px; height: 750px; overflow: hidden;
    background: var(--backdrop);
    font-family: "Jost", "Futura", sans-serif;
  }
  .card {
    position: absolute;
    top: 218px;
    width: 492px; height: 281px;
    border-radius: 16px;
    overflow: hidden;
  }
  .card-front { left: 91px; background: var(--card-white); }
  .card-back { left: 620px; background: var(--slate); display: flex; align-items: center; justify-content: center; }

  .brand {
    position: absolute; left: 28px; top: 50px; width: 200px;
    display: flex; flex-direction: column; align-items: center;
  }
  .brand-mark { width: 118px; height: 118px; }
  .brand-name {
    margin-top: 10px;
    font-weight: 300; font-size: 19px; letter-spacing: 2px;
    color: var(--slate);
  }
  .divider {
    position: absolute; left: 222px; top: 53px;
    width: 1px; height: 165px; background: var(--divider);
  }
  .details { position: absolute; left: 247px; top: 55px; }
  .person-name { font-weight: 400; font-size: 20px; color: var(--slate-dark); line-height: 1.2; }
  .person-role { font-weight: 300; font-size: 14px; color: var(--slate-light); margin-top: 1px; }
  .address {
    margin-top: 12px; font-weight: 400; font-size: 13px;
    letter-spacing: 0.8px; line-height: 1.45; color: var(--ink);
  }
  .contacts { margin-top: 10px; list-style: none; }
  .contacts li {
    display: flex; align-items: center; gap: 7px;
    font-size: 13px; letter-spacing: 0.4px; line-height: 19px; color: var(--ink);
  }
  .contacts svg { width: 12px; height: 12px; flex: none; }
  .band-rule {
    position: absolute; left: 0; right: 0; bottom: 23px;
    height: 1px; background: var(--slate-light);
  }
  .band {
    position: absolute; left: 0; right: 0; bottom: 0;
    height: 21px; background: var(--slate);
  }
  .back-url {
    color: var(--back-text); font-weight: 400; font-size: 16px; letter-spacing: 1.6px;
  }
</style>
</head>
<body>
  <section class="card card-front">
    <div class="brand">
      <svg class="brand-mark" viewBox="0 0 118 118" aria-hidden="true">
        <circle cx="59" cy="59" r="57" fill="var(--slate)"/>
      </svg>
      <div class="brand-name">CEDAR HALL</div>
    </div>
    <div class="divider"></div>
    <div class="details">
      <div class="person-name">Louise-Jane Tredwick</div>
      <div class="person-role">Senior Pastor</div>
      <div class="address">3-4/71 Marlow Street<br>Ridgeford 2163</div>
      <ul class="contacts">
        <li>
          <svg viewBox="0 0 12 12" aria-hidden="true"><path d="M1 4.5C1 2.5 3 1.5 6 1.5S11 2.5 11 4.5V5.5H8.5V4.2H3.5V5.5H1Z M3 6H9L10.5 10.5H1.5Z" fill="var(--slate-dark)"/><circle cx="6" cy="8.3" r="1.1" fill="#fff"/></svg>
          02 95558172
        </li>
        <li>
          <svg viewBox="0 0 12 12" aria-hidden="true"><rect x="0.5" y="2.5" width="11" height="7.5" fill="var(--slate-dark)"/><path d="M0.8 2.8L6 7L11.2 2.8" fill="none" stroke="#fff" stroke-width="1"/></svg>
          info@cedarhallfellowship.example
        </li>
        <li>
          <svg viewBox="0 0 12 12" aria-hidden="true"><g fill="none" stroke="var(--slate-light)" stroke-width="0.9"><circle cx="6" cy="6" r="5"/><ellipse cx="6" cy="6" rx="2.2" ry="5"/><path d="M1 6H11M2 3.3H10M2 8.7H10"/></g></svg>
          www.cedarhallfellowship.example
        </li>
      </ul>
    </div>
    <div class="band-rule"></div>
    <div class="band"></div>
  </section>

  <section class="card card-back">
    <div class="back-url">www.cedarhallfellowship.example</div>
  </section>
</body>
</html>
```